Booklet for meditation CD to match existing CD cover

We need a design for a booklet that matches the meditation CD cover previously designed. It should look like it belongs to the CD as it will be inserted into the cover slot. I hope you can re-use some of the existing artwork. It should incorporate the logo and the text and probably the list of tracks as well. I have attached the original CD cover file, the logo file, photo file and the specs from the CD production company for the 8 page booklet. The spec also includes a cover spec. You can ignore that part. Please put all the text from the CD cover, as well as the track names and the credits from the CD cover into the booklet and the text describing the meditation in full which I have enclosed as a word file.

Target Market(s)

People interested in meditation and personal growth

Font styles to use
Serif

Colors
0555a3
876aae
a54499
e667a6
ee363c

Requirements
Must have
• must match the existing CD cover, must include logo and photo and text from CD cover
• Design, Fonts and colours should match CD cover.

```html
<!DOCTYPE html>
<html lang="en">
<head>
<meta charset="utf-8">
<title>The Open Sky Meditation – CD Booklet</title>
<link rel="stylesheet" href="https://fonts.googleapis.com/css2?family=Cinzel:wght@400;600&family=Roboto+Condensed:ital,wght@0,400;0,700;1,400&display=swap">
<style>
  :root{
    --bg:#e4e0da;
    --ink:#2b2f55;
    --heading:#23407e;
    --accent:#a54499;
    --white:#ffffff;
    --logo:#876aae;
  }
  *{box-sizing:border-box;margin:0;padding:0}
  html,body{width:1200px;height:1200px;overflow:hidden;background:var(--bg)}
  .stage{position:relative;width:1200px;height:1200px;background:var(--bg)}
  .spread{position:absolute;left:322px;width:556px;height:275px;display:flex;box-shadow:0 2px 6px rgba(0,0,0,.25)}
  .spread--1{top:20px}.spread--2{top:314px}.spread--3{top:610px}.spread--4{top:905px}
  .page{position:relative;width:278px;height:275px;overflow:hidden;font-family:"Roboto Condensed",sans-serif;color:var(--ink);font-size:5.1px;line-height:1.28}
  .page + .page{border-left:1px solid rgba(40,40,90,.25)}
  .bg-cover{background:linear-gradient(180deg,#4e5890 0%,#8b86b8 28%,#d9b3cf 55%,#f2b3cf 80%,#e89cc0 100%)}
  .bg-dusk{background:linear-gradient(180deg,#3c4885 0%,#6f73ad 25%,#c6b6d6 50%,#f0bcd4 75%,#ed9fc4 100%)}
  .bg-rise{background:linear-gradient(180deg,#f4c6da 0%,#c5b4d8 40%,#6d6fab 75%,#3d4986 100%)}
  .bg-glow{background:radial-gradient(ellipse at 50% 35%,#fbe7ef 0%,#f1bcd5 35%,#a49cc9 75%,#4a548f 100%)}
  .bg-pink{background:linear-gradient(180deg,#f2b6d0 0%,#f7d3e2 40%,#d5bedc 70%,#b6a6cf 100%)}
  .cols{position:absolute;inset:20px 18px 14px 22px;display:grid;grid-template-columns:1fr 1fr;column-gap:10px}
  .col p{margin-bottom:3px}
  h1,h2,h3{font-family:"Cinzel",serif;font-weight:400;color:var(--heading);line-height:1.02}
  h3{font-size:8.6px;margin:2px 0 3px}
  .h-light{color:var(--white)}
  /* back cover */
  .portrait{position:absolute;left:28px;top:22px;width:80px;height:94px;background:linear-gradient(160deg,#c43a3e,#8d4a6e 50%,#d9a7b8);border:2px solid var(--white)}
  .background-title{position:absolute;left:28px;top:129px;font-size:11px;color:var(--white)}
  .background-text{position:absolute;left:28px;top:146px;width:118px;color:var(--ink)}
  .tracks{position:absolute;right:34px;top:22px;text-align:right;color:var(--white)}
  .tracks h2{font-size:11px;color:var(--white);margin-bottom:4px}
  .tracks ol{list-style:none;font-style:italic;font-size:5.3px;line-height:2.1;color:#f3f0fa}
  .more{position:absolute;right:34px;bottom:30px;width:106px;text-align:right;color:var(--accent);font-weight:700;font-size:5px;line-height:1.6}
  .logo-pill{position:absolute;bottom:30px;height:32px;background:var(--white);border-radius:16px;display:flex;align-items:center;gap:6px;padding:0 14px;font-family:"Roboto Condensed",sans-serif;font-size:15px;color:var(--logo)}
  .logo-pill i{display:block;width:12px;height:12px;border-radius:50%;background:var(--logo)}
  .logo-back{left:8px;width:112px}
  .logo-front{right:6px;width:112px}
  /* front cover */
  .cover-title{position:absolute;top:40px;left:0;right:0;text-align:center;font-size:22px;color:var(--white);line-height:1.1}
  .cover-art{position:absolute;left:88px;top:110px;width:104px;height:165px;border-radius:50px 50px 0 0;background:radial-gradient(ellipse at 50% 40%,#6b4a58 0%,#8a6878 35%,#c48aa8 60%,rgba(233,160,196,0) 75%)}
  .tagline{position:absolute;font-family:"Cinzel",serif;font-size:8.4px;color:var(--white);text-align:center;line-height:1.15}
  .tag-1{left:8px;top:120px;width:76px}
  .tag-2{left:8px;top:188px;width:76px}
  .tag-3{right:8px;top:120px;width:80px}
  /* page 2 */
  .intro{position:absolute;inset:22px 20px 12px 20px;text-align:center}
  .intro h1{font-size:14px;color:var(--white);margin-bottom:8px}
  .intro p{color:var(--white);font-weight:700;font-size:5.6px;line-height:1.7;margin-bottom:6px}
  .intro h2{font-size:11px;color:var(--white);margin:8px 0 10px}
  .stages{list-style:none;text-align:left;margin-left:40px;color:var(--heading);font-weight:700;font-size:5.5px;line-height:2.7}
</style>
</head>
<body>
<main class="stage">

  <section class="spread spread--1">
    <article class="page bg-cover">
      <div class="portrait" role="img" aria-label="Portrait photo of the meditation teacher Mira Holt"></div>
      <h2 class="background-title">Background</h2>
      <p class="background-text">We developed this meditation primarily to be used in workshops as the morning meditation but it can also be used very effectively at home. You may need to use pillows to muffle the sounds during the wild phase. The aim is to bring you into your body, connecting you through movement with both your physical and emotional body and then using that vital and alive connection to open to an experience of Essence.</p>
      <div class="tracks">
        <h2>Tracks</h2>
        <ol>
          <li>1. Shaking</li>
          <li>2. The Flow of Your Wild Energy</li>
          <li>3. Loving Yourself</li>
          <li>4. Focussing the Energy</li>
          <li>5. Centre of Instinct</li>
          <li>6. Sacral Chakra</li>
          <li>7. Power Centre</li>
          <li>8. Heart Chakra</li>
          <li>9. Throat Chakra</li>
          <li>10. Centre of Intuition</li>
          <li>11. Crown Chakra</li>
          <li>12. Silence</li>
          <li>13. Receiving the infinite</li>
          <li>14. Silence</li>
          <li>15. Celebration of Being</li>
        </ol>
      </div>
      <p class="more">If you want to find out more about workshops with Mira Holt, go to www.miraholt-meditation.com</p>
      <div class="logo-pill logo-back"><i></i>Mira Holt</div>
    </article>
    <article class="page bg-cover">
      <h1 class="cover-title">The Open Sky<br>Meditation</h1>
      <div class="cover-art" role="img" aria-label="Illustration of a tree with deep roots on a glowing planet and a figure meditating beneath it"></div>
      <p class="tagline tag-1">A meditation to open to all that you are</p>
      <p class="tagline tag-2">A meditation to fly high in your life</p>
      <p class="tagline tag-3">A meditation to open to your roots and your wings</p>
      <div class="logo-pill logo-front"><i></i>Mira Holt</div>
    </article>
  </section>

  <section class="spread spread--2">
    <article class="page bg-dusk">
      <div class="intro">
        <h1>The Open Sky<br>Meditation</h1>
        <p>For this meditation you'll need a space where you can move freely and preferably have a mattress or soft space for the second and third stages. You'll need a pillow for the second stage.</p>
        <p>The meditation is in 7 stages that start with movement and move towards stillness.</p>
        <h2>The Seven Stages Are</h2>
        <ol class="stages">
          <li>1 Shaking (standing)</li>
          <li>2 Exploring your wild energy (on the floor or mattress)</li>
          <li>3 Loving yourself in your aliveness (on the floor or mattress)</li>
          <li>4 Journeying up through each of the energy centres or chakras in the body (moving mid-way to standing)</li>
          <li>5 Receiving the energy of the infinite standing in that consciousness</li>
          <li>6 Guided back into sitting in meditation for 15 minutes</li>
          <li>7 Celebration and returning to your day</li>
        </ol>
      </div>
    </article>
    <article class="page bg-dusk">
      <div class="cols">
        <div class="col">
          <h3 class="h-light">First Stage:<br>Shaking</h3>
          <p>Stand with your feet about hip distance apart, feet firmly planted on the floor. Let your knees be soft and begin to let your body bounce, generating the shaking from your knees so that everything from your pelvis upwards can move freely. Be aware of your body's limitations. It's not necessary to shake strongly, it can be a gentle movement. Don't shake violently. If anything hurts or you are concerned about your body, either make the movement more gentle or lie on the floor and shake your limbs or don't do it at all.</p>
          <p>Try to keep your whole upper body relaxed, letting go of any holding so that everything can shake gently. Imagine your head is loose. Shake everything that you are thinking and feeling. Bring everything down into your body so that your focus of attention is in your body's aliveness and not in your head. Let your belly, shoulders and jaw be loose. Let your mouth be a little open and relaxed. Let your breathing be as full and easy.</p>
          <p>For this stage, keep any sounds inside.</p>
        </div>
        <div class="col">
          <h3 class="h-light">Second Stage:<br>Exploring Your<br>Wild Energy</h3>
          <p>It's easier to get into your wild nature if you let yourself be down on the floor so you can roll around, let go and move easily. During this stage you let your body be as wild, free and uninhibited as you can. Start by holding the pillow so that you can use your hands to squeeze it and claw into it. Your mouth may even be biting into the pillow. Make sure you let your hips move. Be uncensored. Let your body have the freedom to move in ways that would be outside its regular habits and pattern.</p>
          <p>Keep your eyes closed, opening them only to be sure that you aren't going to hit anything. If you can, let your wild sounds come as well as your wild movements. If that would cause problems, direct your sounds into the pillow. This wild energy may have many different flavours, sometimes all at the same time. It could be wildly happy or angry or sexual. Allow whatever arises and let your body lead you. Beware of going into a repeated pattern of getting angry by beating up someone from the past. Be willing to discover all your energies, not just what you know. Be curious about what is going on in you today. Never mind about</p>
        </div>
      </div>
    </article>
  </section>

  <section class="spread spread--3">
    <article class="page bg-rise">
      <div class="cols">
        <div class="col">
          <p>what was happening last time you did it, let today be new and discover yourself today. Give yourself permission to enjoy your uncensored, wild energy. Breathe fully. Move fully. Use your hands and jaw and pelvis to connect with your wildness.</p>
          <h3>Third Stage:<br>Loving Yourself</h3>
          <p>Now that you've let your energy be wild you'll likely feel a lot of energy running through you. Enjoy! Feel your life, your life energy – whatever shape, colour, movement or temperature – flowing inside you. Let your focus move to soft, deep breathing so that you feel more of yourself. Embrace and befriend all that you discover within yourself. Move softly and gently, maybe stroking yourself as you breathe softly, but fully as a way of saying a total yes to yourself. Enjoy your aliveness. You can relax and let go into the softness of your body. Keep your body gently moving.</p>
        </div>
        <div class="col">
          <h3>Fourth Stage:<br>Journeying Up<br>Through Each of<br>the Energy Centres<br>or Chakras in the<br>Body</h3>
          <p>Focusing: Begin by focusing all the energy in your body down at the base of your body. Imagine white light energy streaming down from your head, from your fingers, from your feet down into the base of your body, the first chakra. Use your breath a little like you would use breath to start a fire, giving the fire more oxygen, more air, to bring your inner fire alive. Imagine you could breathe through the base of your trunk. You can guide the energy by visualising it moving in your body or by sensing it and guiding it, or by physically stroking your body as if you were sweeping the energy to the base of your body.</p>
          <h3>1st Chakra:<br>Instinct – Nature</h3>
          <p>You are bringing your total focus to the centre of instinct that sits at the base of your trunk. We're going on a journey through the chakras or energy centres of your</p>
        </div>
      </div>
    </article>
    <article class="page bg-rise">
      <div class="cols">
        <div class="col">
          <p>body. Even if this is unfamiliar to you, allow yourself to focus your attention in each centre or chakra and imagine your breath is going there. The centre of instinct is at the very base of your body. It is associated with primal energy, an energy that wants to become life, that wants to live. It has a raw quality to it. Think of a lioness protecting her young or animals mating. It is pure instinct, it doesn't have any reflection or consideration in it. It's the beginning stage of life happening.</p>
          <h3>2nd Chakra:<br>Sacral – Sex</h3>
          <p>From there we move the energy up into the sacral centre. This is focused on your sexual nature, your wanting and reaching out to get what you want and to get pleasure. Breathing and focusing on the area of your sex will help you connect with this. There is nothing to do with the energy, just notice the life that is happening there and let it have its natural movement.</p>
          <h3>3rd Chakra:<br>Naval – Power</h3>
          <p>Then we move up to the centre of power. This is the area sometimes known as the hara in martial arts. It's just below the</p>
        </div>
        <div class="col">
          <p>belly button. As you breathe and focus on this area you can connect with your own personal power, the power to stand in your own being as a man or woman and feel your strength there. Let yourself move to standing during this section if you have been down on the mattress or floor. Feel yourself standing on the ground on your human journey as man or woman.</p>
          <h3>4th Chakra: Heart</h3>
          <p>The fourth centre is the heart chakra. Focus on your heart with your breath. Imagine and feel all the wild energies from the lower centres flowing up into your heart and your heart transforming all this wild crazy passionate energy into a calm, loving radiance that fills you and surrounds you giving you a sense of a deeper inner yes to yourself. Bask in this deep inner yes to yourself that is beyond the mind. See your heart centre gives you when you tune in to it and allow it to receive you in your totality. Feel into the boundlessness of your heart and its capacity to hold you, embrace you. Feel how your heart is so much greater than your wounds. And as you connect with your heart energy, feel the sense of an inner mother holding you, the mother of great compassion embracing you. Relax into this and receive this loving energy.</p>
        </div>
      </div>
    </article>
  </section>

  <section class="spread spread--4">
    <article class="page bg-glow">
      <div class="cols">
        <div class="col">
          <h3>5th Chakra: Throat</h3>
          <p>This deep inner yes to yourself moves up into your throat centre, the centre of your unique expression of being. It brings a yes to your voice, to your way of being and living yourself so that you can bring your gifts to the world. Feel into the freedom to live and give of yourself without fear, without censoring yourself, knowing you are good enough. Trusting that your gift is uniquely yours to give and is welcomed by existence.</p>
          <h3>6th Chakra:<br>Third Eye –<br>Intuition</h3>
          <p>And then let that energy of a yes to your being flow up into the centre of intuition, the point between your eyebrows. It's the gateway beyond your physical self, sometimes felt as a deep inner knowing or being in touch with divine wisdom.</p>
          <p>The more you pay attention to this point, entering into a deep listening, the more you will receive. Don't worry if you don't feel anything at first. It's a practice and it may be a sense that you haven't used in a while. Enter with curiosity into the possibility.</p>
        </div>
        <div class="col">
          <h3>7th Chakra: Crown</h3>
          <p>Whatever you find, you let that energy also move upwards to the crown of your head or just above it. Allow your attention to expand out beyond yourself, allowing that connection with spirit that at some level you have known since the beginning of time. You may have had glimpses of this ground of consciousness that is beyond the physical realm. Allow yourself to be still, melting into this ethereal state just as a drop of rain dissolves into the ocean. Enter oneness. No doing, no trying. Simply being with whatever arises as you allow your consciousness to expand.</p>
          <h3>Fifth Stage:<br>Receiving The<br>Energy</h3>
          <p>Receiving the energy of the infinite and standing in that consciousness and giving yourself the delicious gift of complete stillness without any movement for two minutes.</p>
          <h3>Sixth Stage</h3>
          <p>You are guided back, grounding all this energy down into your physical body. Your body still alive from the earlier stages of your journey and still open to receive and be enriched by the Source of existence. Allow</p>
        </div>
      </div>
    </article>
    <article class="page bg-pink">
      <div class="cols">
        <div class="col">
          <p>that flow of energy to enrich and enlighten your physical body, opening each centre in turn: your third eye, your throat, your heart, your power centre, your sex and your root chakra.</p>
          <p>Allow this flow of Spirit back into your being and into the earth beneath your feet, feeling yourself one part of the infinite flow of existence. And feel the flow of your nature rising up to meet Spirit in one eternal, never ending cycle. Stay alive to all that is moving in you and find your way into sitting in stillness.</p>
          <h3>Sitting in<br>Meditation for<br>15 Minutes</h3>
          <p>A word about sitting. To get the most out of any silent sitting meditation, it is recommended that you keep your spine upright as if there were an invisible thread from the crown of your head pulling upwards while your body remains relaxed. It is more important to be comfortable than to contort your body or force it into a position that doesn't let you relax. Ideally you will have three points making contact with the floor. If you know how to sit in the lotus position and can relax there, that's wonderful. If you can sit cross-legged</p>
        </div>
        <div class="col">
          <p>supported by a cushion with both knees touching the floor, that works well. If you are balancing on your sit bones with nothing else to support you you're probably going to end slumping. In that case, it is usually better to either sit against a wall or sit in a chair or stand. With an upright spine you are holding yourself between total relaxation and total attention so that you could spring up like a samurai warrior.</p>
          <p>As you sit silently listening to all the life that flows within you, you may find it helpful to keep your attention on your breath. In any case, any time you find yourself lost in some thought, simply let go and bring yourself back to this present moment.</p>
          <h3>Seventh Stage –<br>Celebration and<br>Returning to<br>Your Day</h3>
          <p>Finally, as the music brings you back to end your meditation, allow it to call you into the beauty of this moment, into a celebration of life and all that it gives you, and especially into a celebration of this wholeness, this totality of being that you are, here, now today. Take this out into your day.</p>
        </div>
      </div>
    </article>
  </section>

</main>
</body>
</html>
```